Business Package for Charitable Company
Lantern Drift
Business Package for Charitable Company - Fund Raising
Creative Brief
Professional
Peter Hollis
President
20400 SW Meadowlark Road Suite C Maple Hollow, OR 97000
555-xxx-xxxx
555-418-xxxx
Peter@lanterndrift.example
www.lanterndrift.example
Will need to get final project files in both AI and word Formatting should include sheet of cards(on 8x11) so can go to printer Letterhead email address needs to be info@lanterndrift.example. Front of Business Card needs to have main company logo. See attached. Also on Envelop no phone numbers or email Folder put place holder for a brief description of who we are on the back side of the folder. Inside location on right hand side provide area for card. Front cover include web address and email info@lanterndrift.example only no address phone number etc. Power Point Template that has title page, bullet page and conclusion page. To be clear we need the final deliverables: FRONT AND BACK BUSINESS CARD SIZE 10 ENVELOPE AND LETTER HEAD POWER POINT PRESENTATION TEMPLATE FOLDER DESIGN WITH FLAPS FOR HOLDING PROPOSAL PAPERWORK I have uploaded from a previous project the items that I need for this project to give you a idea of what I am looking for.
Please incorporate the full tagline information: Share Freely Lift Neighbors Build Futures Want options with all Black background and white and don't include logo image (ie circle) use the file I uploaded that shows lantern standing in as the first "I" in LANTERN in the back of the card until we can take a look at things.
markpdx markpdx
Designers, Please make sure that you use my upload for example only and provide your own creative layout and design I don't need it be the same. Thanks
FONTS AND COLORS FOR LOGO ARE: Font: PerpetuaTiltingMTBold GillSansMT Color: Brown: Pantone 4485 Orange: Pantone 180 Light Orange: Pantone 718 Yellow: Pantone 116

```html
<!DOCTYPE html>
<html lang="en">
<head>
<meta charset="utf-8">
<title>Lantern Drift — Business Card</title>
<link rel="stylesheet" href="https://fonts.googleapis.com/css2?family=Cinzel:wght@700&family=Crimson+Text:wght@400;700&family=Lato:wght@400;700&display=swap">
<style>
  :root {
    --backdrop: #7f7f7f;
    --brown: #6e5219;
    --brown-dark: #5a4212;
    --brown-light: #8c6b26;
    --orange: #d9531e;
    --orange-light: #f2a33a;
    --ink: #4a3a1c;
    --white: #ffffff;
  }
  * { margin: 0; padding: 0; box-sizing: border-box; }
  html, body { width: 1200px; height: 908px; overflow: hidden; }
  body { background: var(--backdrop); position: relative; font-family: "Crimson Text", Georgia, serif; }

  .card {
    position: absolute; top: 104px; width: 400px; height: 700px;
    border-radius: 28px; overflow: hidden;
    box-shadow: 0 10px 24px rgba(0,0,0,.28);
  }

  /* Back */
  .card-back {
    left: 170px;
    background: linear-gradient(160deg, var(--brown-light) 0%, var(--brown) 45%, var(--brown-dark) 100%);
  }
  .back-mark {
    position: absolute; left: 50%; top: 50%; width: 620px;
    transform: translate(-50%, -50%) rotate(90deg);
    text-align: center; color: var(--white);
  }
  .back-mark .wordmark { font-family: "Cinzel", serif; font-weight: 700; font-size: 46px; letter-spacing: 1px; line-height: 1; }
  .back-mark .tagline { font-family: "Lato", sans-serif; font-size: 12px; letter-spacing: 2.4px; text-transform: uppercase; margin-top: 8px; }

  /* Front */
  .card-front { left: 630px; background: var(--white); }
  .scene-fill {
    position: absolute; left: 0; right: 0; bottom: 0; height: 330px;
    background: linear-gradient(180deg, rgba(255,255,255,0) 0%, #fbe1b0 30%, var(--orange-light) 62%, var(--orange) 100%);
  }
  .front-mark { position: absolute; top: 70px; left: 0; right: 0; text-align: center; }
  .front-mark .lockup { display: inline-flex; align-items: center; gap: 10px; }
  .front-mark .dot { width: 36px; height: 36px; border-radius: 50%; background: var(--orange-light); }
  .front-mark .wordmark { font-family: "Cinzel", serif; font-weight: 700; font-size: 28px; color: var(--brown); line-height: 1; }
  .front-mark .tagline { font-family: "Lato", sans-serif; font-size: 9px; letter-spacing: 2px; color: var(--orange); text-transform: uppercase; margin-top: 6px; }

  .person { position: absolute; top: 210px; left: 0; right: 0; text-align: center; }
  .person .name { font-size: 28px; color: var(--brown); line-height: 1.1; }
  .person .role { font-size: 20px; font-weight: 700; color: var(--orange); }

  .contact { position: absolute; top: 320px; left: 40px; color: var(--ink); font-size: 16px; line-height: 1.35; }
  .contact address { font-style: normal; }
  .contact ul { list-style: none; margin-top: 4px; }
  .contact li { display: flex; align-items: center; gap: 8px; }
  .contact .icon { width: 15px; height: 15px; flex: none; }
</style>
</head>
<body>
  <section class="card card-back">
    <div class="back-mark">
      <div class="wordmark">LANTERN DRIFT</div>
      <div class="tagline">Share Freely • Lift Neighbors • Build Futures</div>
    </div>
  </section>

  <section class="card card-front">
    <div class="scene-fill" role="img" aria-label="Hiker silhouette standing on a mountain ridge against an orange sunset sky"></div>

    <div class="front-mark">
      <div class="lockup"><span class="dot"></span><span class="wordmark">LANTERN DRIFT</span></div>
      <div class="tagline">Share • Lift • Build</div>
    </div>

    <div class="person">
      <div class="name">Peter Hollis</div>
      <div class="role">President</div>
    </div>

    <div class="contact">
      <address>20400 SW Meadowlark Road<br>Suite C<br>Maple Hollow, OR 97000</address>
      <ul>
        <li>
          <svg class="icon" viewBox="0 0 16 16"><circle cx="8" cy="8" r="8" fill="#d9531e"/><path d="M5 4.5l1.6-.5 1 2-1 .8a5 5 0 0 0 2.6 2.6l.8-1 2 1-.5 1.6c-3.5 0-6.5-3-6.5-6.5z" fill="#fff"/></svg>
          555-xxx-xxxx
        </li>
        <li>
          <svg class="icon" viewBox="0 0 16 16"><circle cx="8" cy="8" r="8" fill="#d9531e"/><path d="M5 4.5l1.6-.5 1 2-1 .8a5 5 0 0 0 2.6 2.6l.8-1 2 1-.5 1.6c-3.5 0-6.5-3-6.5-6.5z" fill="#fff"/></svg>
          555-418-xxxx
        </li>
        <li>
          <svg class="icon" viewBox="0 0 16 16"><circle cx="8" cy="8" r="8" fill="#d9531e"/><rect x="4" y="5.5" width="8" height="5.5" fill="none" stroke="#fff" stroke-width="1"/><path d="M4 5.5l4 3 4-3" fill="none" stroke="#fff" stroke-width="1"/></svg>
          Peter@lanterndrift.example
        </li>
        <li>
          <svg class="icon" viewBox="0 0 16 16"><circle cx="8" cy="8" r="8" fill="#d9531e"/><circle cx="8" cy="8" r="4" fill="none" stroke="#fff" stroke-width="1"/><path d="M4 8h8M8 4v8" stroke="#fff" stroke-width="1"/></svg>
          www.lanterndrift.example
        </li>
      </ul>
    </div>
  </section>
</body>
</html>
```